Energy Drink label Vumbalo

Design a Label to be used on the packaging label/mock up for a energy drink. The name VUMBALO means Black Bull & Bull ( in the 11 languages in the target country we want to launch ). I would like a in your face energy drink label design. Please see uploaded files as reference . Something out of the box thinking. For 500ml tin can label.

Target Market(s)

Population of Africa

Industry/Entity Type

Energy Drink

Colors
EB3D1F
EC4F4E
F09395
F8D3D4
FCEDEE

Requirements
Must have
• Bold and attractive design ( Black , Red , Silver , White ) as MAIN color scheme, as attached files I uploaded
Nice to have
• option of a white background and also black ( matte / carbon fibre effect )

```html
<!DOCTYPE html>
<html lang="en">
<head>
<meta charset="utf-8">
<title>Vumbalo Energy Drink – Can Label</title>
<link rel="stylesheet" href="https://fonts.googleapis.com/css2?family=Black+Ops+One&family=Oswald:wght@500;700&display=swap">
<style>
  :root {
    --page: #f2f2f3;
    --label-dark: #14121c;
    --label-deep: #221634;
    --violet: #6a2f8f;
    --violet-glow: #9b4fd0;
    --white: #f4f4f6;
    --silver: #c9c9cf;
    --red: #e02a22;
  }
  * { margin: 0; padding: 0; box-sizing: border-box; }
  html, body { width: 1177px; height: 1200px; overflow: hidden; background: var(--page); }
  .canvas { position: relative; width: 1177px; height: 1200px; }

  .label {
    position: absolute; left: 60px; top: 310px; width: 1057px; height: 580px;
    background: var(--label-dark); overflow: hidden;
  }
  .label__art {
    position: absolute; inset: 0;
    background:
      radial-gradient(ellipse 40% 55% at 22% 30%, rgba(155,79,208,.55), transparent 70%),
      radial-gradient(ellipse 35% 50% at 78% 70%, rgba(106,47,143,.6), transparent 70%),
      radial-gradient(ellipse 30% 40% at 50% 95%, rgba(90,60,200,.45), transparent 70%),
      linear-gradient(160deg, var(--label-deep), var(--label-dark) 55%, var(--label-deep));
  }

  .brand {
    position: absolute; left: 0; right: 0; top: 40px;
    display: flex; flex-direction: column; align-items: center;
  }
  .brand__dot {
    width: 200px; height: 200px; border-radius: 50%;
    background: var(--label-dark); border: 6px solid var(--silver);
  }
  .brand__name {
    margin-top: 18px;
    font-family: "Black Ops One", system-ui, sans-serif;
    font-size: 124px; line-height: 1; letter-spacing: 2px; color: var(--white);
  }

  .product {
    position: absolute; left: 300px; top: 400px;
    font-family: "Black Ops One", system-ui, sans-serif;
    font-size: 50px; line-height: .95; color: var(--red);
  }

  .claims {
    position: absolute; left: 600px; top: 396px; list-style: none;
    font-family: "Oswald", sans-serif; font-weight: 500;
    font-size: 30px; line-height: 1.3; color: var(--silver); letter-spacing: 1px;
  }
  .claims li { display: flex; align-items: center; gap: 10px; }
  .claims svg { width: 22px; height: 22px; }

  .facts {
    position: absolute; left: 60px; top: 300px;
    font-family: "Oswald", sans-serif; color: var(--white); text-align: center;
  }
  .fact { margin-bottom: 18px; }
  .fact__value { display: block; font-weight: 700; font-size: 48px; line-height: 1; }
  .fact__unit { display: block; font-weight: 500; font-size: 20px; letter-spacing: 1px; }
</style>
</head>
<body>
<main class="canvas">
  <section class="label">
    <div class="label__art" role="img" aria-label="Dark violet background with glowing purple light streaks and chevrons"></div>

    <div class="brand">
      <div class="brand__dot"></div>
      <h1 class="brand__name">VUMBALO</h1>
    </div>

    <p class="product">ENERGY<br>DRINK</p>

    <ul class="claims">
      <li><svg viewBox="0 0 24 24"><path d="M3 13l6 6L21 5" fill="none" stroke="currentColor" stroke-width="3"/></svg>REFUEL</li>
      <li><svg viewBox="0 0 24 24"><path d="M3 13l6 6L21 5" fill="none" stroke="currentColor" stroke-width="3"/></svg>REHYDRATE</li>
      <li><svg viewBox="0 0 24 24"><path d="M3 13l6 6L21 5" fill="none" stroke="currentColor" stroke-width="3"/></svg>RE-ENERGIZE</li>
    </ul>

    <div class="facts">
      <div class="fact"><span class="fact__value">50</span><span class="fact__unit">CALORIES</span></div>
      <div class="fact"><span class="fact__value">70 G</span><span class="fact__unit">CAFFEINE</span></div>
      <div class="fact"><span class="fact__value">500 ML</span><span class="fact__unit">NET CONTENT</span></div>
    </div>
  </section>
</main>
</body>
</html>
```